New letterhead design for legal, public interest law firm

THIS IS FOR A LETTERHEAD DESIGN CONTEST , PLEASE REFRAIN FROM SUBMITTING JUST LOGO PROPOSALS AND BUSINESS CARD. LOGO AND BUSINESS CARD PROJECTS WILL BE AWARDED TO THE WINNER OF THE LETTERHEAD DESIGN.
Looking for a timeless, elegant and modern design for our letterhead and logo. Our website is www.hlrbvwn.org so you can incorporate the mission, vision and values into the design. As we also included a request for a NEW LOGO design, please be sure to include logo design options.
We are a public interest criminal defense organization that represents indigent people charged with federal crimes. Please weave the mission/vision/values and our practice area into the logo design.
Target Market(s)
Judges, clients, attorneys, family members of our clients.
Industry/Entity Type
Legal
Contact Information for Business Card
Include line for address, direct line, fax, email address, website address. Remember to incorporate NEW LOGO design.
Logo Text
Harbor Legal Advocates Northern Bureau of Westmoor
Requirements
Must have
- Please remember this project is also to design us a NEW LOGO. Please do not incorporate the existing logo into the new letterhead design.
Nice to have
- Nice to see some logo samples incorporating symbolism for justice, California specific imagery.
Should not have
- New logo should NOT have any traditional/typical legal related images (e.g., scales of justice, etc.)

```html
<!DOCTYPE html>
<html lang="en">
<head>
<meta charset="utf-8">
<title>Harbor Legal Advocates Northern Bureau of Westmoor – Letterhead</title>
<link rel="stylesheet" href="https://fonts.googleapis.com/css2?family=Poppins:wght@300;400;500;600;700&family=Kaushan+Script&display=swap">
<style>
  :root {
    --backdrop: #303030;
    --paper: #ffffff;
    --navy: #24338c;
    --orange: #f39200;
    --ink: #161616;
    --tick: #1f2a5a;
  }
  * { margin: 0; padding: 0; box-sizing: border-box; }
  html, body { width: 1200px; height: 1200px; overflow: hidden; background: var(--backdrop); }
  body { font-family: "Poppins", sans-serif; color: var(--ink); }

  .letterhead {
    position: absolute; left: 208px; top: 93px;
    width: 783px; height: 1013px;
    background: var(--paper); overflow: hidden;
  }
  .header-art { position: absolute; left: 0; top: 0; }

  .brand-name {
    position: absolute; left: 29px; top: 135px; width: 156px;
    transform: translateY(-50%);
    text-align: center; color: var(--navy);
    font-weight: 600; font-size: 27px; line-height: 32px; letter-spacing: 3px;
  }

  .line { position: absolute; transform: translateY(-50%); white-space: nowrap; }

  .date-label { left: 510px; top: 110px; font-size: 14px; font-weight: 500; }
  .date-rule { position: absolute; left: 556px; top: 113px; width: 101px; border-top: 1px solid #333; }

  .intro { left: 81px; top: 256px; font-size: 12.9px; font-weight: 600; }
  .heading { font-size: 13.5px; font-weight: 600; }
  .heading--large { font-size: 17.5px; }
  .body-text { font-size: 13.6px; font-weight: 400; }

  .paragraph {
    position: absolute; left: 78px; top: 388px;
    font-size: 13.3px; line-height: 22.6px; white-space: nowrap;
  }

  .check-item { position: absolute; left: 86px; transform: translateY(-50%); display: flex; align-items: flex-start; }
  .check-item svg { width: 14px; height: 14px; flex: none; margin-top: 2px; }
  .check-item span { margin-left: 9px; font-size: 13.6px; line-height: 22.6px; white-space: nowrap; }
  .check-item.multi { transform: none; }

  .sign-off { left: 77px; top: 823px; font-size: 17px; font-weight: 300; color: #333; }
  .signature { left: 73px; top: 862px; font-family: "Kaushan Script", cursive; font-size: 33px; color: #2a2a2a; }

  .contact { position: absolute; top: 959px; transform: translateY(-50%); display: flex; align-items: center; font-size: 12.5px; color: #1d1d3a; white-space: nowrap; }
  .contact svg { width: 11px; height: 11px; margin-right: 8px; }
  .divider { position: absolute; top: 951px; height: 16px; border-left: 1.3px solid #222; }

  .footer-band { position: absolute; left: 0; bottom: 0; width: 100%; height: 13px; background: var(--navy); }
</style>
</head>
<body>
<main class="letterhead">
  <svg class="header-art" width="783" height="230" viewBox="0 0 783 230">
    <rect x="499" y="0" width="284" height="42" fill="var(--navy)"/>
    <path d="M100,-5 H469 A18,18 0 0 1 487,13 V42 H100 Z" fill="var(--orange)" stroke="var(--paper)" stroke-width="6"/>
    <path d="M24,-10 H110 A79,79 0 0 1 189,69 V135 A82.5,82.5 0 0 1 24,135 Z" fill="var(--navy)" stroke="var(--paper)" stroke-width="6"/>
    <circle cx="106.5" cy="135" r="78" fill="var(--paper)"/>
  </svg>
  <div class="brand-name">HLA<br>NBW</div>

  <div class="line date-label">Date:</div>
  <div class="date-rule"></div>

  <p class="line intro">Lorem Ipsum is simply dummy text of the printing and typesetting industry. Lorem Ipsum has been</p>

  <div class="check-item" style="top:289px"><svg viewBox="0 0 14 14"><rect x="1" y="2" width="11" height="11" rx="2" fill="none" stroke="var(--tick)" stroke-width="1.6"/><path d="M3.5,7 L6.5,10 L13,2.5" fill="none" stroke="var(--tick)" stroke-width="2"/></svg><span>Lorem Ipsum is simply</span></div>
  <div class="check-item" style="top:311px"><svg viewBox="0 0 14 14"><rect x="1" y="2" width="11" height="11" rx="2" fill="none" stroke="var(--tick)" stroke-width="1.6"/><path d="M3.5,7 L6.5,10 L13,2.5" fill="none" stroke="var(--tick)" stroke-width="2"/></svg><span>Lorem Ipsum is simply</span></div>
  <div class="check-item" style="top:334px"><svg viewBox="0 0 14 14"><rect x="1" y="2" width="11" height="11" rx="2" fill="none" stroke="var(--tick)" stroke-width="1.6"/><path d="M3.5,7 L6.5,10 L13,2.5" fill="none" stroke="var(--tick)" stroke-width="2"/></svg><span>Lorem Ipsum is simply</span></div>

  <h2 class="line heading" style="left:78px; top:371px">Initial Access</h2>
  <p class="paragraph">Lorem Ipsum is simply dummy text of the printing and typesetting industry. Lorem Ipsum has been the<br>industry's standard dummy text ever since the 1500s, when an unknown printer took a galley of type and<br>scrambled it to make a type specimen book. It has survived not only five centuries, but also the leap into</p>

  <h2 class="line heading" style="left:76px; top:488px">Execution</h2>
  <p class="line body-text" style="left:79px; top:510px">Lorem Ipsum is simply dummy text of the printing and</p>

  <div class="check-item" style="top:538px"><svg viewBox="0 0 14 14"><rect x="1" y="2" width="11" height="11" rx="2" fill="none" stroke="var(--tick)" stroke-width="1.6"/><path d="M3.5,7 L6.5,10 L13,2.5" fill="none" stroke="var(--tick)" stroke-width="2"/></svg><span>Lorem Ipsum is simply</span></div>
  <div class="check-item" style="top:560px"><svg viewBox="0 0 14 14"><rect x="1" y="2" width="11" height="11" rx="2" fill="none" stroke="var(--tick)" stroke-width="1.6"/><path d="M3.5,7 L6.5,10 L13,2.5" fill="none" stroke="var(--tick)" stroke-width="2"/></svg><span>Lorem Ipsum is simply</span></div>
  <div class="check-item" style="top:583px"><svg viewBox="0 0 14 14"><rect x="1" y="2" width="11" height="11" rx="2" fill="none" stroke="var(--tick)" stroke-width="1.6"/><path d="M3.5,7 L6.5,10 L13,2.5" fill="none" stroke="var(--tick)" stroke-width="2"/></svg><span>Lorem Ipsum is simply</span></div>

  <h2 class="line heading heading--large" style="left:76px; top:627px">Capabilties</h2>
  <p class="line body-text" style="left:79px; top:653px">Lorem Ipsum is simply dummy text of the printing and</p>

  <div class="check-item" style="top:681px"><svg viewBox="0 0 14 14"><rect x="1" y="2" width="11" height="11" rx="2" fill="none" stroke="var(--tick)" stroke-width="1.6"/><path d="M3.5,7 L6.5,10 L13,2.5" fill="none" stroke="var(--tick)" stroke-width="2"/></svg><span>Lorem Ipsum is simply dummy text of the printing and typesetting industry. Lorem Ipsum</span></div>
  <div class="check-item" style="top:707px"><svg viewBox="0 0 14 14"><rect x="1" y="2" width="11" height="11" rx="2" fill="none" stroke="var(--tick)" stroke-width="1.6"/><path d="M3.5,7 L6.5,10 L13,2.5" fill="none" stroke="var(--tick)" stroke-width="2"/></svg><span>Lorem Ipsum is simply dummy text of the</span></div>
  <div class="check-item multi" style="top:724px"><svg viewBox="0 0 14 14"><rect x="1" y="2" width="11" height="11" rx="2" fill="none" stroke="var(--tick)" stroke-width="1.6"/><path d="M3.5,7 L6.5,10 L13,2.5" fill="none" stroke="var(--tick)" stroke-width="2"/></svg><span>Lorem Ipsum is simply dummy text of the printing and typesetting industry.<br>Lorem Ipsum has been the industry's standard dummy text ever since the<br>1500s, when an unknown printer took a galley of type and scrambled it to</span></div>

  <p class="line sign-off">Warm Regards</p>
  <p class="line signature">Ned Calloway</p>

  <div class="contact" style="left:78px"><svg viewBox="0 0 12 12"><path d="M6,0.5 A4,4 0 0 1 10,4.5 C10,7.5 6,11.5 6,11.5 C6,11.5 2,7.5 2,4.5 A4,4 0 0 1 6,0.5 Z M6,3 A1.5,1.5 0 1 0 6,6 A1.5,1.5 0 1 0 6,3 Z" fill="var(--navy)" fill-rule="evenodd"/></svg>Westmoor, CA</div>
  <div class="divider" style="left:220px"></div>
  <div class="contact" style="left:238px"><svg viewBox="0 0 12 12"><path d="M2.5,1 L4.5,1 L5.3,3.8 L4,5 C4.8,6.7 5.3,7.2 7,8 L8.2,6.7 L11,7.5 L11,9.5 C11,10.5 10,11 9,11 C4.5,10.5 1.5,7.5 1,3 C1,2 1.5,1 2.5,1 Z" fill="none" stroke="var(--navy)" stroke-width="1.3"/></svg>(555) 218-0473</div>
  <div class="divider" style="left:368px"></div>
  <div class="contact" style="left:382px"><svg viewBox="0 0 12 12"><rect x="0.5" y="2" width="11" height="8" fill="var(--navy)"/><path d="M0.5,2.5 L6,6.5 L11.5,2.5" fill="none" stroke="#fff" stroke-width="1"/></svg>NorvaleLLC@mailbox.com</div>
  <div class="divider" style="left:569px"></div>
  <div class="contact" style="left:584px"><svg viewBox="0 0 12 12"><g fill="none" stroke="var(--navy)" stroke-width="1"><circle cx="6" cy="6" r="5"/><ellipse cx="6" cy="6" rx="2.2" ry="5"/><path d="M1,6 H11 M1.8,3.5 H10.2 M1.8,8.5 H10.2"/></g></svg>www.hlrbvwn.org</div>

  <div class="footer-band"></div>
</main>
</body>
</html>
```